Letterhead and envelope design

Using current logo and colours I would like to have a new design done for a stationary set to be printed.

The new files should include logo, web and email address as well as,mailing address and phone number

Dov Harmsby
Harmsby Construction Inc
Box 27 Site 18 RR5
Okotoks AB
T4K 2B9
Cell : 403-555-2917
Email: dov@harmsbyconstruction.example
web: harmsbyconstruction.example

```html
<!DOCTYPE html>
<html lang="en">
<head>
<meta charset="utf-8">
<title>Harmsby Construction – Stationery Set</title>
<link href="https://fonts.googleapis.com/css2?family=Arimo:wght@400;700&family=Pinyon+Script&display=swap" rel="stylesheet">
<style>
  :root {
    --navy: #0d2f5e;
    --orange: #d38a1f;
    --paper: #efefef;
    --ink: #2b2b2b;
    --muted: #555;
    --backdrop: #9c9c9c;
  }
  * { margin: 0; padding: 0; box-sizing: border-box; }
  html, body { width: 1200px; height: 1011px; overflow: hidden; }
  body {
    background: var(--backdrop);
    font-family: "Arimo", Arial, sans-serif;
    color: var(--ink);
    position: relative;
  }
  .sheet {
    position: absolute;
    background: var(--paper);
    box-shadow: 0 1px 4px rgba(0,0,0,.25);
    overflow: hidden;
  }
  .letterhead { left: 85px; top: 149px; width: 508px; height: 718px; }
  .envelope-back { left: 632px; top: 351px; width: 509px; height: 241px; background: transparent; box-shadow: none; overflow: visible; }
  .envelope-front { left: 632px; top: 626px; width: 509px; height: 241px; }

  .brand { position: absolute; display: flex; align-items: center; gap: 7px; }
  .brand-dot { border-radius: 50%; background: var(--navy); flex: none; }
  .brand-name {
    font-weight: 700; color: var(--navy); line-height: 1.15;
    letter-spacing: .2px;
  }
  .letterhead .brand { left: 190px; top: 25px; }
  .letterhead .brand-dot { width: 54px; height: 54px; }
  .letterhead .brand-name { font-size: 10.5px; }
  .envelope-front .brand { left: 38px; top: 34px; }
  .envelope-front .brand-dot { width: 50px; height: 50px; }
  .envelope-front .brand-name { font-size: 10px; }

  .letter { position: absolute; left: 54px; top: 168px; width: 402px; font-size: 8.3px; line-height: 12px; }
  .letter p { margin-bottom: 12px; text-align: justify; }
  .letter .date { margin-bottom: 12px; }
  .letter .recipient { margin-bottom: 24px; text-align: left; }
  .letter .salutation { margin-bottom: 12px; }
  .letter .body { margin-bottom: 12px; }
  .closing { margin-top: 30px; }
  .signature { font-family: "Pinyon Script", cursive; font-size: 16px; line-height: 20px; margin-top: 4px; }

  .contacts { position: absolute; list-style: none; font-size: 8.2px; line-height: 10.4px; color: var(--muted); }
  .contacts li { display: flex; align-items: center; gap: 5px; }
  .contacts svg { width: 7px; height: 7px; flex: none; }
  .letterhead .contacts { left: 45px; top: 641px; }
  .envelope-front .contacts { left: 39px; top: 166px; font-size: 7.4px; line-height: 9.8px; }

  .footer-band {
    position: absolute; left: 0; right: 0; height: 25px;
    background: linear-gradient(to right, var(--navy) 0 var(--split), var(--orange) var(--split) 100%);
    color: #fff; font-size: 8.3px; display: flex; align-items: center;
    white-space: nowrap;
  }
  .letterhead .footer-band { top: 683px; --split: 456px; padding-left: 44px; }
  .envelope-front .footer-band { top: 205px; height: 23px; --split: 464px; padding-left: 39px; font-size: 7.6px; }
  .band-dot {
    position: absolute; top: 50%; transform: translate(-50%, -50%);
    border-radius: 50%; background: var(--navy); border: 2px solid #fff;
  }
  .letterhead .band-dot { left: 442px; width: 30px; height: 30px; }
  .envelope-front .band-dot { left: 452px; width: 27px; height: 27px; }
</style>
</head>
<body>

<section class="sheet letterhead">
  <div class="brand">
    <span class="brand-dot"></span>
    <span class="brand-name">HARMSBY<br>CONSTRUCTION</span>
  </div>

  <article class="letter">
    <p class="date">01 January 2050</p>
    <p class="recipient">Quenby Supply Ltd.<br>PO Box 4410 Ridgeway St<br>Lindale City Country 4410</p>
    <p class="salutation">Dear Marla Quenby,</p>
    <p class="body">Lorem ipsum dolor sit amet, consectetuer adipiscing elit, sed diam nonummy nibh euismod tincidunt ut laoreet dolore magna aliquam erat volutpat. Ut wisi enim ad minim veniam, quis nostrud exerci tation ullamcorper suscipit lobortis nisl ut aliquip ex ea commodo consequat. Duis dolore te feugait nulla facilisi. Nam liber tempor cum soluta nobis eleifend option congue nihil imperdiet doming id quod mazim placerat facer possim assum. Lorem ipsum dolor sit amet, consectetuer adipiscing elit, sed diam nonummy nibh euismod tincidunt ut laoreet dolore magna aliquam erat volutpat. Ut wisi enim ad minim veniam, quis nostrud exerci tation ullamcorper suscipit lobortis nisl ut aliquip ex ea commodo consequat.</p>
    <p class="body">Consectetuer adipiscing elit, sed diam nonummy nibh euismod tincidunt ut laoreet dolore magna aliquam erat volutpat. Ut wisi enim ad minim veniam, quis nostrud exerci tation ullamcorper suscipit lobortis nisl ut aliquip ex ea commodo consequat. Consectetuer adipiscing elit, sed diam nonummy nibh euismod tincidunt ut laoreet dolore magna aliquam erat volutpat. Ut wisi enim ad minim veniam, quis nostrud exerci tation ullamcorper suscipit lobortis nisl ut aliquip ex ea commodo consequat.</p>
    <p class="body">Consectetuer adipiscing elit, sed diam nonummy nibh euismod tincidunt ut laoreet dolore magna aliquam erat volutpat. Ut wisi enim ad minim veniam, quis nostrud exerci tation ullamcorper suscipit lobortis nisl ut aliquip ex ea commodo consequat. Consectetuer adipiscing elit, sed diam nonummy nibh euismod tincidunt ut laoreet dolore magna aliquam erat volutpat. Ut wisi enim ad minim veniam, quis nostrud exerci tation ullamcorper suscipit lobortis nisl ut aliquip ex ea commodo consequat.</p>
    <p class="closing">Sincerely Yours</p>
    <p class="signature">Dov Harmsby</p>
  </article>

  <ul class="contacts">
    <li><svg viewBox="0 0 8 8"><rect x="2" y="0.5" width="4" height="7" rx="0.6" fill="none" stroke="#333" stroke-width="0.9"/></svg>403-555-2917</li>
    <li><svg viewBox="0 0 8 8"><rect x="0.5" y="1.5" width="7" height="5" fill="none" stroke="#333" stroke-width="0.9"/><path d="M0.5 1.5 4 4.5 7.5 1.5" fill="none" stroke="#333" stroke-width="0.9"/></svg>dov@harmsbyconstruction.example</li>
    <li><svg viewBox="0 0 8 8"><circle cx="4" cy="4" r="3.5" fill="none" stroke="#333" stroke-width="0.9"/><path d="M0.5 4h7M4 0.5c-2 2-2 5 0 7M4 0.5c2 2 2 5 0 7" fill="none" stroke="#333" stroke-width="0.7"/></svg>harmsbyconstruction.example</li>
  </ul>

  <div class="footer-band">
    Harmsby Construction Inc, 000 Sample Road, Exampleton, Nowhere Province
    <span class="band-dot"></span>
  </div>
</section>

<section class="sheet envelope-back">
  <svg width="509" height="241" viewBox="0 0 509 241">
    <rect x="0" y="0" width="509" height="241" fill="var(--paper)"/>
    <path d="M9 60 Q9 56 12 56 L497 56 Q500 56 500 60 L500 232 L9 232 Z" fill="none" stroke="#d8d8d8" stroke-width="1"/>
    <path d="M0 0 L509 0 L494 72 Q492 79 484 79 L25 79 Q17 79 15 72 Z" fill="var(--navy)"/>
    <circle cx="255" cy="39" r="20" fill="var(--navy)" stroke="#fff" stroke-width="2"/>
  </svg>
</section>

<section class="sheet envelope-front">
  <div class="brand">
    <span class="brand-dot"></span>
    <span class="brand-name">HARMSBY<br>CONSTRUCTION</span>
  </div>

  <ul class="contacts">
    <li><svg viewBox="0 0 8 8"><rect x="2" y="0.5" width="4" height="7" rx="0.6" fill="none" stroke="#333" stroke-width="0.9"/></svg>403-555-2917</li>
    <li><svg viewBox="0 0 8 8"><rect x="0.5" y="1.5" width="7" height="5" fill="none" stroke="#333" stroke-width="0.9"/><path d="M0.5 1.5 4 4.5 7.5 1.5" fill="none" stroke="#333" stroke-width="0.9"/></svg>dov@harmsbyconstruction.example</li>
    <li><svg viewBox="0 0 8 8"><circle cx="4" cy="4" r="3.5" fill="none" stroke="#333" stroke-width="0.9"/><path d="M0.5 4h7M4 0.5c-2 2-2 5 0 7M4 0.5c2 2 2 5 0 7" fill="none" stroke="#333" stroke-width="0.7"/></svg>harmsbyconstruction.example</li>
  </ul>

  <div class="footer-band">
    Harmsby Construction Inc, 000 Sample Road, Exampleton, Nowhere Province
    <span class="band-dot"></span>
  </div>
</section>

</body>
</html>
```